Tolvek Card Design

IT consulting services - my company focuses on delivering value add for clients through sourcing services, strategic and project consulting services, as well as delivering office fitout project managment services.
We also offer IT Interim managment services - to fill the gap when looking for executive roles.
I use orange and blue as my corporate colours
I am after a simple design with my details on the front and my services not the back
Industry/Entity Type
It Company
Contact Information for Business Card
Martin Oskrey
Director
Tolvek Solutions
Martin.Oskrey@TolvekSolutions.com.au
www.TolvekSolutions.com.au
m: +61 427580916
On Rear of card:
Interim Management
Project and Strategy Consulting
Sourcing Services
Commercial fit-out management

```html
<!DOCTYPE html>
<html lang="en">
<head>
<meta charset="utf-8">
<title>Tolvek Solutions – Business Card</title>
<link rel="stylesheet" href="https://fonts.googleapis.com/css2?family=Noto+Sans:wght@400;700&display=swap">
<style>
  :root {
    --backdrop-centre: #fbfdfd;
    --backdrop-edge: #dde6e7;
    --paper: #dcdfdc;
    --paper-line: rgba(0,0,0,0.035);
    --orange: #d86f00;
    --navy: #0b1f66;
    --white: #ffffff;
  }
  * { margin: 0; padding: 0; box-sizing: border-box; }
  html, body {
    width: 1200px; height: 716px; overflow: hidden;
  }
  body {
    position: relative;
    background: radial-gradient(ellipse at 50% 55%, var(--backdrop-centre) 0%, var(--backdrop-edge) 100%);
    font-family: "Noto Sans", Verdana, sans-serif;
  }
  .card {
    position: absolute;
    top: 193px;
    width: 540px; height: 329px;
    overflow: hidden;
    background:
      repeating-linear-gradient(90deg, var(--paper-line) 0 1px, transparent 1px 4px),
      var(--paper);
    box-shadow: 0 1px 2px rgba(0,0,0,0.08);
  }
  .card--front { left: 38px; }
  .card--back { left: 622px; }
  .card__tear {
    position: absolute; inset: 0;
    width: 540px; height: 329px;
  }
  .brand {
    position: absolute;
    display: flex; align-items: center;
    color: var(--navy);
    font-weight: 700;
  }
  .brand__square { background: var(--navy); flex: none; }
  .brand--large { left: 82px; top: 134px; gap: 50px; }
  .brand--large .brand__square { width: 60px; height: 60px; }
  .brand--large .brand__name { font-size: 30px; line-height: 30px; letter-spacing: 0.3px; }
  .brand--small { left: 406px; top: 254px; gap: 33px; }
  .brand--small .brand__square { width: 20px; height: 20px; }
  .brand--small .brand__name { font-size: 12px; line-height: 12px; letter-spacing: -0.2px; }
  .tagline {
    position: absolute; left: 410px; top: 145px;
    color: var(--white);
    font-weight: 700; font-size: 16px; line-height: 16px; letter-spacing: 0.4px;
  }
  .services {
    position: absolute; left: 28px; top: 34px;
    list-style: none;
    color: var(--white);
    font-size: 13px; line-height: 20px; letter-spacing: 0.4px;
  }
  .contact {
    position: absolute; left: 28px; top: 197px;
    color: var(--white);
    font-size: 13px; line-height: 16px; letter-spacing: 0.5px;
  }
  .contact__name { font-weight: 700; font-size: 15px; line-height: 17px; letter-spacing: 0.3px; }
  .contact__role { margin-bottom: 13px; }
  .contact__mobile { margin-bottom: 13px; }
</style>
</head>
<body>
  <section class="card card--front" aria-label="Card front">
    <svg class="card__tear" viewBox="0 0 540 329" aria-hidden="true">
      <polygon fill="var(--orange)" stroke="var(--white)" stroke-width="5"
        points="600,-5 600,340 385,340 385,329 380,316 386,304 381,292 387,278 383,266 379,252 385,240 382,228 388,214 383,200 380,188 386,176 382,162 387,150 381,138 384,124 379,112 385,98 382,86 387,72 381,60 384,46 379,34 385,22 382,10 386,0 386,-5"/>
    </svg>
    <div class="brand brand--large">
      <span class="brand__square"></span>
      <span class="brand__name">Tolvek<br>Solutions</span>
    </div>
    <p class="tagline">Innovative<br>Business<br>Solutions</p>
  </section>

  <section class="card card--back" aria-label="Card back">
    <svg class="card__tear" viewBox="0 0 540 329" aria-hidden="true">
      <polygon fill="var(--orange)" stroke="var(--white)" stroke-width="5"
        points="-10,-5 -10,340 395,340 395,329 399,318 393,306 398,294 392,282 397,268 394,256 400,244 394,232 397,218 392,206 398,194 395,180 400,168 393,156 397,142 392,130 398,118 394,104 399,92 393,80 396,66 391,54 397,42 393,28 398,16 394,4 394,-5"/>
    </svg>
    <ul class="services">
      <li>Interim Management</li>
      <li>Project and Strategy Consulting</li>
      <li>Sourcing Services</li>
      <li>Commercial Fit-out Management</li>
    </ul>
    <div class="contact">
      <p class="contact__name">Martin Oskrey</p>
      <p class="contact__role">Director</p>
      <p class="contact__mobile">Mobile: +61 427 580 916</p>
      <p>E-mail: martin.oskrey@tolveksolutions.com.au</p>
      <p>Web: www.tolveksolutions.com.au</p>
    </div>
    <div class="brand brand--small">
      <span class="brand__square"></span>
      <span class="brand__name">Tolvek<br>Solutions</span>
    </div>
  </section>
</body>
</html>
```